Branvique needs a business Card Design

We are looking for a business card Design for our new Managed Service Provider Company, Branvique. Branvique encompasses everything IT for the average medium sized business. Our primary services are help desk support, cyber-security (malware and ransomware protection), and Disaster Recovery systems. We would like the design to have a very clean and professional look, with a very minimalist feel.

Target Market(s)

Medium to large sized businesses

Industry/Entity Type

It Service

Contact Information for Business Card

Name GoesHere
name@branvique.com
O: 555-382-6047
C: 555-731-5820

Font styles to use
Other font styles liked:
• Poppins Font Only Please

Colors

Designer to choose only greyscale colors for use in the design.

Requirements
Must have
• Logo included
Nice to have
• Cutting Edge, innovative, minimalistic, elegant

```html
<!DOCTYPE html>
<html lang="en">
<head>
<meta charset="UTF-8">
<title>Branvique Business Card</title>
<link href="https://fonts.googleapis.com/css2?family=Poppins:wght@300;400;600&display=swap" rel="stylesheet">
<style>
  :root {
    --stage: #d6d6d6;
    --card: #1f1f1f;
    --ink: #ffffff;
    --ink-soft: #d4d4d4;
    --rule: rgba(255,255,255,0.7);
  }
  * { margin: 0; padding: 0; box-sizing: border-box; }
  html, body { width: 1200px; height: 1021px; overflow: hidden; }
  body {
    background: var(--stage);
    font-family: "Poppins", sans-serif;
    color: var(--ink);
    position: relative;
  }
  .card {
    position: absolute;
    left: 250px;
    width: 700px;
    height: 400px;
    background: var(--card);
    box-shadow: 0 10px 30px rgba(0,0,0,0.25);
  }
  .card--front { top: 60px; }
  .card--back { top: 561px; }

  .front-wordmark {
    position: absolute;
    inset: 0;
    display: flex;
    align-items: center;
    justify-content: center;
    font-weight: 300;
    font-size: 30px;
    letter-spacing: 0.35em;
    padding-left: 0.35em;
  }

  .brand {
    position: absolute;
    left: 0;
    top: 0;
    width: 330px;
    height: 400px;
    display: flex;
    align-items: center;
    justify-content: center;
  }
  .brand__name {
    font-weight: 300;
    font-size: 24px;
    letter-spacing: 0.35em;
    padding-left: 0.35em;
    white-space: nowrap;
  }
  .divider {
    position: absolute;
    left: 330px;
    top: 105px;
    width: 1.5px;
    height: 190px;
    background: var(--rule);
  }
  .contact {
    position: absolute;
    left: 375px;
    top: 110px;
  }
  .contact__name {
    font-weight: 600;
    font-size: 25px;
    line-height: 1.15;
    white-space: nowrap;
  }
  .contact__role {
    font-weight: 400;
    font-size: 15px;
    color: var(--ink-soft);
    margin-bottom: 16px;
  }
  .contact__list { list-style: none; }
  .contact__item {
    display: flex;
    align-items: center;
    gap: 9px;
    font-size: 18px;
    font-weight: 400;
    line-height: 29px;
    white-space: nowrap;
  }
  .contact__icon { width: 15px; height: 15px; flex: none; }
</style>
</head>
<body>
  <section class="card card--front" aria-label="Card front">
    <div class="front-wordmark">BRANVIQUE</div>
  </section>

  <section class="card card--back" aria-label="Card back">
    <div class="brand"><span class="brand__name">BRANVIQUE</span></div>
    <div class="divider"></div>
    <div class="contact">
      <div class="contact__name">Daniel Reyes</div>
      <div class="contact__role">Founder</div>
      <ul class="contact__list">
        <li class="contact__item">
          <svg class="contact__icon" viewBox="0 0 24 24"><path fill="#fff" d="M6.6 10.8a15 15 0 0 0 6.6 6.6l2.2-2.2a1 1 0 0 1 1-.25 11.4 11.4 0 0 0 3.6.57 1 1 0 0 1 1 1V20a1 1 0 0 1-1 1A17 17 0 0 1 3 4a1 1 0 0 1 1-1h3.5a1 1 0 0 1 1 1c0 1.25.2 2.45.57 3.57a1 1 0 0 1-.25 1z"/></svg>
          <span>555-382-6047</span>
        </li>
        <li class="contact__item">
          <svg class="contact__icon" viewBox="0 0 24 24"><rect x="6" y="2" width="12" height="20" rx="2" fill="none" stroke="#fff" stroke-width="2"/><line x1="10" y1="18" x2="14" y2="18" stroke="#fff" stroke-width="2"/></svg>
          <span>555-731-5820</span>
        </li>
        <li class="contact__item">
          <svg class="contact__icon" viewBox="0 0 24 24"><rect x="2" y="5" width="20" height="14" fill="none" stroke="#fff" stroke-width="2"/><path d="M2 5l10 8 10-8" fill="none" stroke="#fff" stroke-width="2"/></svg>
          <span>name@branvique.com</span>
        </li>
        <li class="contact__item">
          <svg class="contact__icon" viewBox="0 0 24 24" fill="none" stroke="#fff" stroke-width="1.8"><circle cx="12" cy="12" r="10"/><ellipse cx="12" cy="12" rx="4.5" ry="10"/><line x1="2" y1="12" x2="22" y2="12"/></svg>
          <span>www.branvique.com</span>
        </li>
      </ul>
    </div>
  </section>
</body>
</html>
```